Asia based real estate financing firm needs and AWESOME design for a biz card -Harbor Lending Circle

Looking for a stylish, & corporate-looking business card for a real estate financing brokerage firm in Asia, offering global mortgage loans. I uploaded our current logos. We would like to add a splash of color (perhaps the house icon) or any other suggestions are open. For the winning designer, we have a lot of work! Thanks and best of luck!

Target Market(s)

Real estate investors globally. We want to look more like a BANK and NOT a real estate company. Please don't play up on a "house" design.

Industry/Entity Type

Banking

Contact Information for Business Card

Harbor Lending Circle
Peter Wilks
Co-Founder | Partner

14 Cassia Lane, Suite 310
Singapore 047219
www.hlc-example.asia
peterwilks@hlc-example.asia
+65 555-0142
WeChat: peterwilks

Colors

Designer to choose colors to be used in the design.

Requirements
Must have
• Must have the standard business requirements for a card; name, address, email, etc
• Can be horizontal or vertical.
Nice to have
• It would be great to see some sort of variation to the logo with a pop of color. Red is good as we're in Asia, however, other options work as well.
• Our tag line is - Lending Beyond Limits. It doesn't have to be on the card but might be nice.
• I'd like to start seeing our tagline within the cards as well. - Lending Beyond Limits.
• Also, please add our location. The location for this card is Singapore so perhaps it can be highlighted or emphasised in some way.
• Singapore | Hong Kong | Shanghai | Manila
• As we will soon open an office in Shanghai, having an option for both languages would be great.
Should not have
• I'm exceited and open to your creativity ... knock it out of the park!

```html
<!DOCTYPE html>
<html lang="en">
<head>
<meta charset="utf-8">
<title>Harbor Lending Circle – Business Card</title>
<link rel="stylesheet" href="https://fonts.googleapis.com/css2?family=Cinzel:wght@400&family=Open+Sans:wght@400;600&display=swap">
<style>
  :root {
    --backdrop: #1b1b1d;
    --card: #141416;
    --card-edge: #232326;
    --accent-red: #e3202a;
    --name-blue: #5b6fd0;
    --ink-light: #eeeeee;
    --rule-grey: #8a8a8e;
  }
  * { box-sizing: border-box; margin: 0; padding: 0; }
  html, body {
    width: 1200px; height: 960px; overflow: hidden;
    background: var(--backdrop);
  }
  .sheet {
    width: 1200px; height: 960px;
    display: flex; flex-direction: column; align-items: center; justify-content: center;
    gap: 40px;
  }
  .card {
    width: 700px; height: 400px;
    background: radial-gradient(ellipse at 40% 30%, #1e1e21 0%, var(--card) 70%);
    border: 1px solid var(--card-edge);
    border-radius: 4px;
    box-shadow: 0 14px 30px rgba(0,0,0,.55);
    position: relative;
  }

  /* Company name: plain text in the body font, one colour, one weight */
  .company-name {
    font-family: "Open Sans", sans-serif;
    font-weight: 600;
    color: var(--ink-light);
    display: flex; align-items: center; gap: 14px;
  }
  .company-name__square {
    width: 14px; height: 14px; background: var(--accent-red); flex: none;
  }

  /* Front */
  .card--front {
    display: flex; flex-direction: column; align-items: center; justify-content: center;
  }
  .card--front .company-name { font-size: 38px; }
  .tagline {
    margin-top: 34px;
    display: flex; align-items: center; gap: 16px;
    font-family: "Cinzel", serif;
    font-size: 22px;
    letter-spacing: 3px;
    color: var(--ink-light);
  }
  .tagline__rule {
    width: 90px; height: 1px;
    background: linear-gradient(90deg, transparent, var(--rule-grey));
  }
  .tagline__rule--right { background: linear-gradient(90deg, var(--rule-grey), transparent); }

  /* Back */
  .card--back { display: flex; align-items: center; }
  .back-company {
    width: 330px; display: flex; justify-content: center;
  }
  .card--back .company-name {
    font-size: 24px; flex-direction: column; gap: 10px; text-align: center; line-height: 1.3;
  }
  .divider {
    width: 2px; height: 250px; background: var(--accent-red);
  }
  .contact { padding-left: 34px; }
  .contact__name {
    font-family: "Cinzel", serif;
    font-size: 26px; color: var(--name-blue); letter-spacing: 1px;
  }
  .contact__role {
    font-family: "Open Sans", sans-serif; font-size: 17px; color: var(--ink-light);
    margin-bottom: 16px;
  }
  .contact__address {
    font-family: "Open Sans", sans-serif; font-size: 16px; color: var(--ink-light);
    line-height: 1.4; margin-bottom: 8px;
  }
  .contact__list { list-style: none; }
  .contact__item {
    display: flex; align-items: center; gap: 10px;
    font-family: "Open Sans", sans-serif; font-size: 16px; color: var(--ink-light);
    line-height: 1.65;
  }
  .contact__icon { width: 16px; height: 16px; flex: none; }
</style>
</head>
<body>
<main class="sheet">

  <section class="card card--front" aria-label="Card front">
    <div class="company-name"><span class="company-name__square"></span>Harbor Lending Circle</div>
    <div class="tagline">
      <span class="tagline__rule"></span>
      <span>Lending Beyond Limits</span>
      <span class="tagline__rule tagline__rule--right"></span>
    </div>
  </section>

  <section class="card card--back" aria-label="Card back">
    <div class="back-company">
      <div class="company-name"><span class="company-name__square"></span>Harbor Lending<br>Circle</div>
    </div>
    <div class="divider"></div>
    <div class="contact">
      <p class="contact__name">Peter Wilks</p>
      <p class="contact__role">Co-Founder | Partner</p>
      <p class="contact__address">14 Cassia Lane, Suite 310<br>Singapore 047219</p>
      <ul class="contact__list">
        <li class="contact__item">
          <svg class="contact__icon" viewBox="0 0 16 16" aria-hidden="true"><path fill="#e3202a" d="M3.5 1.5l2.3 2.8-1.3 1.6c.9 2 2.5 3.6 4.5 4.5l1.6-1.3 2.8 2.3-1.6 2.1C6.8 13 3 9.2 1.4 3.1z"/></svg>
          +65 555-0142
        </li>
        <li class="contact__item">
          <svg class="contact__icon" viewBox="0 0 16 16" aria-hidden="true"><rect x="1.5" y="3.5" width="13" height="9" fill="#e3202a"/><path d="M1.5 3.8L8 9l6.5-5.2" stroke="#141416" stroke-width="1.3" fill="none"/></svg>
          peterwilks@hlc-example.asia
        </li>
        <li class="contact__item">
          <svg class="contact__icon" viewBox="0 0 16 16" aria-hidden="true"><g fill="none" stroke="#e3202a" stroke-width="1.4"><circle cx="8" cy="8" r="6.3"/><ellipse cx="8" cy="8" rx="2.7" ry="6.3"/><path d="M1.7 8h12.6M2.8 4.8h10.4M2.8 11.2h10.4"/></g></svg>
          www.hlc-example.asia
        </li>
        <li class="contact__item">
          <svg class="contact__icon" viewBox="0 0 16 16" aria-hidden="true"><g fill="none" stroke="#e3202a" stroke-width="1.4"><ellipse cx="6.5" cy="6.5" rx="5" ry="4"/><path d="M3.5 9.6l-1 2.6 3-1.6"/><path d="M10.5 8.2c2 .3 3.8 1.5 3.8 3 0 .8-.4 1.4-1 1.9l.5 1.9-2-1.1c-.5.1-1 .2-1.5.2"/></g></svg>
          WeChat: peterwilks
        </li>
      </ul>
    </div>
  </section>

</main>
</body>
</html>
```